White Cane Law Awareness Poster

Steady Harbor is a disability advocacy organization in Indiana. We are working on a project with the Hollow Creek Council of Vision Allies. Our organizations need a design for a poster to promote awareness of Indiana's White Cane law. This poster will be displayed in local libraries, businesses, and other public places.

The poster should catch people's attention, and briefly explain that drivers have to yield for pedestrians who are blind who have white canes or seeing eye dogs.

The poster should be designed with people with low vision in mind. This means large text in a clear font, with good contrast between the text and the background. The text should be in a sans serif font that is clear and easy to read, with no italics or script fonts. There should not be a "busy" picture or pattern behind the text.

The poster should also include a reference to the relevant laws. We have attached a document with those references.

Finally, the poster should include the logos of Steady Harbor and the Hollow Creek Council of Vision Allies, which we have included as attachments.

We have also included an attachment with a photo of the old White Cane Law poster, just to show an example of what we DO NOT want.

Industry/Entity Type

Non-Profit

Font styles to use
Sans Serif

Requirements
Must have
• The poster should also include a reference to the relevant laws. We have attached a document with those references.
• Finally, the poster should include the logos of Steady Harbor and the Hollow Creek Council of Vision Allies, which we have included as attachments.

```html
<!DOCTYPE html>
<html lang="en">
<head>
<meta charset="utf-8">
<title>White Cane Law Awareness Poster</title>
<link rel="stylesheet" href="https://fonts.googleapis.com/css2?family=Arimo:wght@700&family=Roboto+Condensed:wght@700&display=swap">
<style>
  :root {
    --backdrop: #8a8a8a;
    --red: #e30613;
    --deep: #1a0000;
    --black: #0b0b0b;
    --white: #ffffff;
    --ink-blue: #1f2f8f;
  }
  html, body {
    margin: 0;
    width: 909px;
    height: 1200px;
    overflow: hidden;
    background: var(--backdrop);
  }
  .poster {
    position: absolute;
    left: 73px;
    top: 60px;
    width: 763px;
    height: 1080px;
    background: var(--white);
    font-family: "Arimo", Arial, sans-serif;
  }
  .hero {
    position: absolute;
    left: 0; top: 0;
    width: 763px; height: 550px;
    background: linear-gradient(180deg, var(--deep) 0%, #7a0006 45%, var(--red) 88%);
  }
  .headline {
    position: absolute;
    left: 0; top: 8px;
    width: 763px;
    margin: 0;
    text-align: center;
    font-size: 285px;
    line-height: 1;
    letter-spacing: -0.065em;
    color: var(--white);
    text-shadow: -8px 8px 0 var(--black);
  }
  .question {
    position: absolute;
    left: 76px; top: 268px;
    margin: 0;
    font-family: "Roboto Condensed", "Arial Narrow", sans-serif;
    font-size: 92px;
    line-height: 82px;
    color: var(--white);
  }
  .law-name {
    position: absolute;
    left: 76px; top: 462px;
    margin: 0;
    font-family: "Roboto Condensed", "Arial Narrow", sans-serif;
    font-size: 76px;
    line-height: 76px;
    color: var(--black);
  }
  .figure-art {
    position: absolute;
    left: 510px; top: 268px;
    width: 230px; height: 282px;
    background: linear-gradient(180deg, #2a0003, #120000);
    border-radius: 6px;
  }
  .law-text {
    position: absolute;
    left: 0; top: 550px;
    width: 763px; height: 300px;
    background: var(--black);
    color: var(--white);
    margin: 0;
    box-sizing: border-box;
    padding-top: 40px;
    text-align: center;
    font-size: 37px;
    line-height: 45px;
  }
  .law-text .highlight { color: var(--red); }
  .slogan {
    position: absolute;
    left: 0; top: 850px;
    width: 763px; height: 65px;
    background: var(--red);
    color: var(--white);
    margin: 0;
    text-align: center;
    font-size: 38px;
    line-height: 65px;
    letter-spacing: 0.02em;
  }
  .partners {
    position: absolute;
    left: 0; top: 915px;
    width: 763px; height: 165px;
    display: flex;
    align-items: center;
    justify-content: center;
    gap: 70px;
  }
  .partner {
    display: flex;
    align-items: center;
    gap: 10px;
    font-size: 20px;
    line-height: 24px;
    color: var(--black);
  }
  .partner-mark {
    width: 22px; height: 22px;
    border-radius: 50%;
    background: var(--black);
    flex: none;
  }
  .partner.harbor { color: var(--ink-blue); }
  .partner.harbor .partner-mark { background: var(--ink-blue); }
</style>
</head>
<body>
  <main class="poster">
    <section class="hero">
      <h1 class="headline">STOP</h1>
      <p class="question">Are you<br>aware?</p>
      <p class="law-name">Indiana Law</p>
      <div class="figure-art" role="img" aria-label="Pictogram of a person in dark glasses holding a white cane and walking with a guide dog on a leash"></div>
    </section>
    <p class="law-text">Requires drives to come to a<br>complete stop when encoutering<br>a pedestrian crossing a street<br>and <span class="highlight">guided by a dog</span> or<br><span class="highlight">carrying a white cane</span></p>
    <p class="slogan">STOP AND SAVE A LIFE</p>
    <footer class="partners">
      <div class="partner council"><span class="partner-mark"></span><span>Hollow Creek Council<br>of Vision Allies</span></div>
      <div class="partner harbor"><span class="partner-mark"></span><span>Steady Harbor</span></div>
    </footer>
  </main>
</body>
</html>
```